B2B EDM Banner Design- Specialist Tech Company

We need a new top-of-email banner for our EDM campaigns for Varnel Brix (www.varnelbrix-example.com
). This banner will sit at the top of every email and must immediately signal the brand, look modern and professional, and be visually aligned with the tech/IT audience.
Size of the banner: Around 728x90 - it must fit at the top of an email blast.
Purpose of the Banner
Establish a strong, recognizable brand identity across all Varnel Brix EDMs
visually consistent with existing banners created for other brands (see reference examples provided)
Communicate Varnel Brix’s value proposition at a glance
Brand Name
Varnel Brix
Tagline (must appear in the banner)
“11,322 whitepapers from 726 companies”
Design Requirements
Style & Tone
Modern, clean, and professional
Tech-centric look and feel
High-quality, sleek, and corporate
Eye-catching but not cluttered
Should feel premium and authoritative
Layout & Composition
Full-width banner for email header
Horizontal orientation similar to the Plomtar and Quindle Staff Archive examples
Include space for the brand name/logo prominently on the left or centered
Integrate the tagline in a readable, secondary position
Optional: a subtle background texture or tech-related abstract pattern (circuitry, network nodes, gradient, etc.)
No busy imagery—should feel clean and trustworthy
Color Palette
Use colors consistent with Varnel Brix branding from www.varnelbrix-example.com
Blues, greys, blacks, and tech-style gradients preferred
Should feel consistent with a B2B IT audience
Typography
Clean, sans-serif fonts (professional/tech-aligned)
Brand name should be bold and prominent
Tagline should be smaller, but still readable on desktop and mobile
Imagery (if used)
Abstract tech shapes, network visuals, geometric patterns, or gradient overlays
Avoid photography of people
Keep imagery subtle so text remains legible
Call-to-Action Button (optional)
None required in this banner (unlike the HR examples)
Banner should remain a pure brand header
Deliverables
Final banner in PNG and JPG formats
2–3 design variations (if possible) for A/B testing
Dimensions optimized for EDM: ~600–700px wide (standard email width), proportionate height

```html
<!DOCTYPE html>
<html lang="en">
<head>
<meta charset="UTF-8">
<title>Varnel Brix – Email Header Banner</title>
<link rel="stylesheet" href="https://fonts.googleapis.com/css2?family=Montserrat:wght@700;800&family=Roboto:wght@500;700&family=Roboto+Condensed:wght@600&display=swap">
<style>
  :root {
    --stage-grey: #c8c8c8;
    --navy-deep: #0a1a3a;
    --navy-mid: #0f3560;
    --glow-blue: #1a8fc8;
    --brand-blue: #0f9ee0;
    --white: #ffffff;
    --map-tone: #164a78;
  }
  * { margin: 0; padding: 0; box-sizing: border-box; }
  html, body {
    width: 1200px;
    height: 774px;
    overflow: hidden;
    background: var(--stage-grey);
  }
  .canvas {
    position: relative;
    width: 1200px;
    height: 774px;
  }
  .banner {
    position: absolute;
    left: 0;
    top: 187px;
    width: 1200px;
    height: 400px;
    overflow: hidden;
    background:
      radial-gradient(ellipse 420px 300px at 110px 200px, rgba(26,143,200,0.75), rgba(26,143,200,0) 70%),
      linear-gradient(90deg, var(--navy-mid) 0%, #103562 40%, var(--navy-deep) 100%);
  }
  .network-globe {
    position: absolute;
    left: -10px;
    top: 0;
    width: 232px;
    height: 400px;
    border-radius: 0 200px 200px 0;
    background: radial-gradient(circle at 40% 50%, rgba(40,170,230,0.55), rgba(20,110,180,0.25) 60%, rgba(20,90,160,0.05) 100%);
  }
  .world-map {
    position: absolute;
    left: 918px;
    top: 41px;
    width: 250px;
    height: 122px;
    border-radius: 40px;
    background: radial-gradient(ellipse at 50% 45%, rgba(22,74,120,0.75), rgba(22,74,120,0.2) 75%, rgba(22,74,120,0) 100%);
  }
  .market-graphic {
    position: absolute;
    left: 1019px;
    top: 285px;
    width: 156px;
    height: 96px;
    border-radius: 20px;
    background: radial-gradient(ellipse at 50% 50%, rgba(15,158,224,0.22), rgba(15,158,224,0.06) 70%, rgba(15,158,224,0) 100%);
  }
  .brand-lockup {
    position: absolute;
    left: 337px;
    top: 119px;
    display: flex;
    align-items: center;
    gap: 22px;
  }
  .brand-mark {
    width: 78px;
    height: 78px;
    border-radius: 50%;
    background: var(--brand-blue);
  }
  .brand-text { width: 312px; }
  .brand-name {
    font-family: "Montserrat", sans-serif;
    font-weight: 800;
    font-size: 42px;
    line-height: 1;
    color: var(--white);
    letter-spacing: 0.5px;
    white-space: nowrap;
    padding-bottom: 6px;
    border-bottom: 1.5px solid var(--brand-blue);
  }
  .brand-tagline {
    margin-top: 6px;
    font-family: "Montserrat", sans-serif;
    font-weight: 700;
    font-size: 12px;
    letter-spacing: 8.6px;
    color: var(--white);
    white-space: nowrap;
  }
  .value-line {
    position: absolute;
    left: 336px;
    top: 216px;
    display: flex;
    align-items: baseline;
    white-space: nowrap;
  }
  .value-figure {
    font-family: "Roboto", sans-serif;
    font-weight: 700;
    font-size: 55px;
    line-height: 1;
    color: var(--brand-blue);
    letter-spacing: -1px;
  }
  .value-words {
    font-family: "Roboto Condensed", sans-serif;
    font-weight: 600;
    font-size: 29.5px;
    color: var(--white);
    margin: 0 8px 0 7px;
  }
  .value-words.last { margin-right: 0; }
</style>
</head>
<body>
<div class="canvas">
  <header class="banner">
    <div class="network-globe" role="img" aria-label="Glowing network globe made of connected nodes and lines"></div>
    <div class="world-map" role="img" aria-label="Faint world map silhouette"></div>
    <div class="market-graphic" role="img" aria-label="Small market trend chart graphic"></div>

    <div class="brand-lockup">
      <div class="brand-mark"></div>
      <div class="brand-text">
        <div class="brand-name">VARNEL BRIX</div>
        <div class="brand-tagline">FOR IT PROFESSIONALS</div>
      </div>
    </div>

    <p class="value-line">
      <span class="value-figure">11322</span>
      <span class="value-words">Whitepapers from</span>
      <span class="value-figure">726</span>
      <span class="value-words last">Companies</span>
    </p>
  </header>
</div>
</body>
</html>
```